Landing page for a sports website

we have a sports tracking and management website and require a web site.
the site should have the ability to have 2 options for selection the first being a competitions portal the other a club portal there should be a about us page and a contact us page
the site should be dynamic and vibrant and be easily recognisable as a multiple sports page
we also have www.velorinote.com and would like it to compliment that site
i would like to have some form of animation regarding sports occur when you click the login option if that is possible
the site is www.vlnsports.com and I have attached the logo in both 3d and standard
we also require a design several templates for information pages please see www.tallyhusk.com as an example of how it should look but with a sports theme
Target Market(s)
This will be used for primarily team based sports
Industry/Entity Type
Management
Number of Pages Required
3 page
Requirements
Must have
- the ability to change the logo and names of the site
- i.e. from vlnsports to vlnschools at a later date

```html
<!DOCTYPE html>
<html lang="en">
<head>
<meta charset="utf-8">
<title>VLN Sports</title>
<link href="https://fonts.googleapis.com/css2?family=Raleway:wght@200;300;400;600;700;800&family=Libre+Baskerville:wght@400;700&display=swap" rel="stylesheet">
<style>
  :root {
    --white: #ffffff;
    --brand-blue: #1ba3cf;
    --brand-orange: #e1602a;
    --login-blue: #1592c2;
    --signup-red: #d23a2e;
    --portal-orange: #d5622d;
    --portal-blue: #0387b6;
    --band-blue: #0a87b6;
    --band-deep: #0a6f98;
    --footer-blue: #0985b4;
    --press-ink: #23343f;
    --dot-dark: #234a5a;
  }
  * { box-sizing: border-box; margin: 0; padding: 0; }
  html, body { width: 1200px; height: 890px; overflow: hidden; }
  body { font-family: 'Raleway', sans-serif; background: var(--white); position: relative; }

  .site-header { position: absolute; top: 0; left: 0; width: 1200px; height: 83px; background: var(--white); }
  .brand { position: absolute; left: 111px; top: 18px; display: flex; align-items: center; gap: 8px; }
  .brand-mark { width: 14px; height: 14px; border-radius: 50%; background: var(--brand-blue); }
  .brand-name { font-size: 30px; font-weight: 800; color: var(--brand-blue); letter-spacing: 1px; line-height: 44px; }
  .auth { position: absolute; top: 34px; right: 111px; display: flex; gap: 7px; }
  .auth a { display: block; height: 23px; padding: 0 12px; border: 2px solid; border-radius: 4px; font-size: 13px; line-height: 19px; text-decoration: none; font-weight: 400; }
  .auth .login { color: #1f5d78; border-color: var(--login-blue); }
  .auth .signup { color: #7a2a22; border-color: var(--signup-red); }

  .hero { position: absolute; top: 83px; left: 0; width: 1200px; height: 614px; overflow: hidden; }
  .hero-photo { position: absolute; inset: 0;
    background:
      linear-gradient(180deg, rgba(0,0,0,0) 62%, rgba(225,232,238,0.85) 82%, #e9eef2 100%),
      radial-gradient(ellipse at 85% 20%, rgba(255,255,255,0.45), rgba(255,255,255,0) 45%),
      linear-gradient(180deg, #0f6196 0%, #2f86bd 40%, #6eaad3 70%, #a9c9de 100%); }
  .hero-content { position: absolute; top: 0; left: 0; width: 1200px; text-align: center; color: var(--white); }
  .hero-title { position: absolute; top: 170px; width: 1200px; font-size: 56px; font-weight: 200; letter-spacing: 1px; }
  .hero-text { position: absolute; top: 251px; width: 1200px; font-size: 17.5px; font-weight: 300; line-height: 28px; }
  .portals { position: absolute; top: 464px; left: 280px; display: flex; gap: 29px; }
  .portal { width: 305px; height: 67px; border-radius: 16px; color: var(--white); font-size: 16px; font-weight: 700; letter-spacing: 2px; line-height: 67px; text-align: center; text-decoration: none; }
  .portal-competition { background: var(--portal-orange); }
  .portal-club { background: var(--portal-blue); }
  .slider-dots { position: absolute; top: 577px; left: 566px; display: flex; gap: 5px; }
  .slider-dots span { width: 13px; height: 13px; border-radius: 50%; background: var(--white); border: 2px solid #7fa7bb; }
  .slider-dots span.active { background: var(--dot-dark); border-color: #cfe0e8; }

  .press { position: absolute; top: 697px; left: 0; width: 1200px; height: 124px;
    background: linear-gradient(180deg, var(--band-deep) 0%, var(--band-blue) 35%, var(--band-blue) 100%);
    border-bottom: 1px solid #0b7aa5; }
  .press-label { position: absolute; top: 34px; width: 1200px; text-align: center; color: var(--white); font-size: 12.5px; font-weight: 600; letter-spacing: 0.3px; }
  .press-list { position: absolute; top: 66px; left: 216px; width: 770px; display: flex; justify-content: space-between; align-items: center; color: var(--press-ink); }
  .press-list li { list-style: none; font-size: 16px; font-weight: 700; font-family: 'Raleway', sans-serif; }

  .site-footer { position: absolute; top: 821px; left: 0; width: 1200px; height: 69px; background: var(--footer-blue); color: var(--white); }
  .copyright { position: absolute; left: 111px; top: 26px; font-size: 13px; font-weight: 600; }
  .social { position: absolute; left: 1032px; top: 18px; display: flex; gap: 3px; }
  .social a { width: 28px; height: 28px; border-radius: 50%; border: 1.5px solid var(--white); display: block; }
</style>
</head>
<body>
  <header class="site-header">
    <div class="brand"><span class="brand-mark"></span><span class="brand-name">VLN Sports</span></div>
    <nav class="auth">
      <a class="login" href="#">LOGIN</a>
      <a class="signup" href="#">SIGN UP</a>
    </nav>
  </header>

  <section class="hero">
    <div class="hero-photo" role="img" aria-label="Skier leaping against a blue sky above snowy mountain peaks"></div>
    <div class="hero-content">
      <h1 class="hero-title">VLN SPORTS</h1>
      <p class="hero-text">Neque porro quisquam est qui dolorem ipsum quia<br>dolor sit amet, consectetur, adipisci velit...</p>
    </div>
    <div class="portals">
      <a class="portal portal-competition" href="#">COMPETITION PORTAL</a>
      <a class="portal portal-club" href="#">CLUB PORTAL</a>
    </div>
    <div class="slider-dots"><span class="active"></span><span></span><span></span><span></span></div>
  </section>

  <section class="press">
    <p class="press-label">FEATURED AS IN</p>
    <ul class="press-list">
      <li>Harborline Ledger</li>
      <li>Fenwright</li>
      <li>KTVR 9</li>
      <li>Market Lantern</li>
      <li>ByteHarbor</li>
      <li>Pacific Courier</li>
    </ul>
  </section>

  <footer class="site-footer">
    <p class="copyright">©2015 Company Name, All Rights Reserved</p>
    <div class="social">
      <a href="#" aria-label="Social profile"></a>
      <a href="#" aria-label="Social feed"></a>
    </div>
  </footer>
</body>
</html>
```